Corwin Ashgrove

I am a songwriter and would like to include a bio, pictures, discography, CD covers and access to some of my music

Target Market(s)

Music Lovers, songwriters publishers

Coding

Coded - Design and coding required

Number of Pages Required

5+ page

Requirements
Must have
• Pictures of my CD covers, pictures of me and either my Music or links to my music
Nice to have
Should not have
• cartoons

```html
<!DOCTYPE html>
<html lang="en">
<head>
<meta charset="utf-8">
<title>Corwin Ashgrove — Songwriter</title>
<link href="https://fonts.googleapis.com/css2?family=Josefin+Sans:wght@400;600;700&display=swap" rel="stylesheet">
<style>
:root{
  --bg:#000;
  --panel:#141414;
  --line:#3a3a3a;
  --yellow:#f5c400;
  --purple:#8a4fb3;
  --white:#fff;
  --muted:#bdbdbd;
}
*{box-sizing:border-box;margin:0;padding:0}
html,body{width:1200px;height:2948px;overflow:hidden;background:var(--bg)}
body{font-family:"Josefin Sans",sans-serif;color:var(--white);position:relative}
.abs{position:absolute}
/* header */
.site-header{left:0;top:0;width:1200px;height:56px;background:#000;border-bottom:1px solid #1c1c1c}
.brand{left:80px;top:16px;font-size:24px;font-weight:700;color:var(--yellow);line-height:26px}
.nav{left:240px;top:20px;display:flex;font-size:15px}
.nav a{color:var(--white);text-decoration:none;width:128px}
.nav a.active{color:var(--yellow)}
.nav a:nth-child(4){width:112px}
.search{left:808px;top:16px;width:192px;height:26px;background:#fff;display:flex}
.search span{flex:1;color:#777;font-size:12px;padding:7px 8px}
.search i{width:30px;background:var(--yellow)}
.social{display:flex;gap:8px}
.social i{width:22px;height:22px;background:var(--yellow);border-radius:3px;display:block}
/* hero */
.hero-photo{left:140px;top:96px;width:480px;height:620px;border-radius:50%;background:radial-gradient(circle at 50% 40%,#b9a48c 0%,#6b5443 35%,#201610 65%,#000 80%)}
.hero-title{left:632px;top:236px;font-size:34px;font-weight:700;line-height:44px}
.hero-title .hl{color:var(--yellow)}
.hero-text{left:632px;top:340px;width:440px;font-size:14px;line-height:20px;color:#e6e6e6}
.btn{display:inline-flex;align-items:center;justify-content:center;font-size:15px;font-weight:600;height:42px;text-decoration:none;color:#fff}
.btn-solid{background:var(--purple)}
.btn-line{border:2px solid var(--yellow)}
/* sections */
.section-title{font-size:32px;font-weight:700;color:var(--yellow)}
.section-sub{font-size:14px;color:#e6e6e6}
.arrow{width:44px;height:44px;border-radius:50%;border:2px solid var(--yellow);display:flex;align-items:center;justify-content:center}
.feature-card{left:64px;top:948px;width:640px;height:512px;border-radius:18px;overflow:hidden;background:linear-gradient(135deg,#3a2a1a,#9a5a18 35%,#c9a06a 60%,#5a4a3a)}
.feature-card .rating{right:30px;top:24px;font-size:16px;display:flex;gap:8px;align-items:center}
.feature-card .play{left:282px;top:210px;width:76px;height:76px;border-radius:50%;background:rgba(0,0,0,.45);border:2px solid #fff}
.feature-card .song{left:110px;top:370px;font-size:30px;font-weight:700;color:var(--yellow)}
.feature-card .artist{left:110px;top:408px;font-size:18px}
.pill{height:28px;padding:0 14px;font-size:13px;display:flex;align-items:center;border-radius:4px}
.top-panel{left:736px;top:948px;width:396px;height:540px;background:var(--panel);border:2px solid var(--line);border-radius:14px}
.top-panel h3{position:absolute;left:24px;top:20px;font-size:22px;color:var(--yellow);line-height:26px}
.burger{right:22px;top:26px;width:24px}
.burger i{display:block;height:3px;background:var(--yellow);margin-bottom:5px}
.track{left:24px;width:350px;height:104px;border-bottom:1px solid var(--line)}
.track .thumb{left:0;top:0;width:124px;height:92px;border-radius:6px;background:linear-gradient(135deg,#4b3a2b,#9b7a55)}
.track .thumb b{position:absolute;left:44px;top:28px;width:36px;height:36px;border-radius:50%;border:2px solid #fff;background:rgba(0,0,0,.4)}
.track .name{left:144px;top:4px;font-size:16px;color:var(--yellow);font-weight:600}
.track .by{left:144px;top:26px;font-size:13px}
.track .meta{left:144px;top:46px;font-size:11px;color:var(--muted)}
.track .ago{left:144px;top:64px;font-size:13px}
.track .price{right:0;top:64px;font-size:13px;color:var(--yellow)}
/* event */
.event-band{left:0;top:1580px;width:1200px;height:460px;background:linear-gradient(180deg,#000 0%,#2a0a02 30%,#7a2508 60%,#d0520f 78%,#3a0e02 100%)}
.event-photo{left:220px;top:1660px;width:320px;height:380px;background:radial-gradient(ellipse at 50% 45%,#b49a82 0%,#6a4b3a 40%,rgba(40,15,5,0) 72%)}
.event-kicker{left:672px;top:1656px;font-size:34px;font-weight:700;color:var(--yellow)}
.event-date{left:672px;top:1702px;font-size:56px;font-weight:700;display:flex;align-items:center;gap:12px}
.event-date i{width:36px;height:4px;background:#fff;display:block}
.event-text{left:672px;top:1788px;width:470px;font-size:14px;line-height:20px;color:#eee}
/* news */
.news-card{top:2240px;width:338px;height:320px}
.news-card p{position:absolute;left:44px;bottom:20px;right:20px;font-size:16px;line-height:20px;color:var(--yellow);font-weight:600;text-shadow:0 1px 2px #000}
/* footer */
.footer-line{left:80px;top:2640px;width:1040px;height:1px;background:#2a2a2a}
.footer-photo{left:88px;top:2680px;width:136px;height:176px;background:linear-gradient(160deg,#9bb2c8,#6b5a48 60%,#e8e8e8)}
.footer-text{left:256px;top:2688px;width:340px;font-size:12px;line-height:18px;color:#ddd}
.footer-col h4{font-size:15px;color:var(--yellow);margin-bottom:12px;font-weight:600}
.footer-col a{display:block;font-size:12px;color:#fff;text-decoration:none;line-height:24px}
.email{display:flex;width:300px;height:38px;margin-top:6px}
.email span{flex:1;background:#fff;color:#777;font-size:12px;padding:12px 10px}
.email i{width:44px;background:var(--yellow);display:flex;align-items:center;justify-content:center}
.copyright{left:0;top:2912px;width:1200px;text-align:center;font-size:14px;color:var(--yellow)}
</style>
</head>
<body>

<header class="site-header abs">
  <div class="brand abs">Ashgrove</div>
  <nav class="nav abs">
    <a class="active" href="#">Home</a><a href="#">About Us</a><a href="#">Event</a><a href="#">Blog</a><a href="#">Contact</a>
  </nav>
  <div class="search abs"><span>Search Here Music...</span><i></i></div>
  <div class="social abs" style="left:1032px;top:17px"><i></i><i></i><i></i><i></i><i></i></div>
</header>

<section class="hero">
  <div class="hero-photo abs" role="img" aria-label="Portrait of Corwin Ashgrove in a white shirt, soft vignette"></div>
  <h1 class="hero-title abs">This Month's<br><span class="hl">Record Breaking Albums !</span></h1>
  <p class="hero-text abs">Dream your moments, Lanterns In June, Paper Boats, Slow River, Autumn Porch Song, Endless.<br><br>Things: Mile Marker Nine, Quiet Harbor Lights, Salt And Cedar, and many more...</p>
  <div class="abs" style="left:632px;top:472px;display:flex;gap:20px">
    <a class="btn btn-solid" href="#" style="width:176px">Listen Now</a>
    <a class="btn btn-line" href="#" style="width:176px">Download Now</a>
  </div>
</section>

<section class="recent">
  <h2 class="section-title abs" style="left:64px;top:820px">Recently Played</h2>
  <p class="section-sub abs" style="left:64px;top:868px">Lorem Ipsum is simply dummy text of the printing and typesetter.</p>
  <div class="arrow abs" style="left:1014px;top:842px"><svg width="14" height="14" viewBox="0 0 14 14"><path d="M9 2L4 7l5 5" stroke="#fff" stroke-width="2.4" fill="none"/></svg></div>
  <div class="arrow abs" style="left:1076px;top:842px"><svg width="14" height="14" viewBox="0 0 14 14"><path d="M5 2l5 5-5 5" stroke="#fff" stroke-width="2.4" fill="none"/></svg></div>

  <article class="feature-card abs" role="img" aria-label="Album cover for Lanterns In June by Corwin Ashgrove: flames, a coffee cup and scattered photographs">
    <div class="rating abs"><svg width="18" height="18" viewBox="0 0 20 20"><path d="M10 1l2.7 6 6.3.6-4.8 4.3 1.4 6.3L10 15l-5.6 3.2 1.4-6.3L1 7.6 7.3 7z" fill="#f5c400"/></svg>5/35</div>
    <div class="play abs"><svg width="72" height="72" viewBox="0 0 76 76"><path d="M31 24l22 14-22 14z" fill="#fff"/></svg></div>
    <div class="song abs">Lanterns In June</div>
    <div class="artist abs">Mira Holt</div>
    <div class="pill abs" style="left:0;bottom:24px;background:var(--purple);border-radius:0 4px 4px 0">Details</div>
    <div class="pill abs" style="right:0;bottom:24px;background:var(--purple);border-radius:4px 0 0 4px">5k views</div>
  </article>

  <aside class="top-panel abs">
    <h3>Weekly<br>Top 15</h3>
    <div class="burger abs"><i></i><i></i><i></i></div>
    <div class="track abs" style="top:100px"><div class="thumb abs" role="img" aria-label="Album cover for Quiet Harbor Lights"><b></b></div><div class="name abs">Quiet Harbor Lights</div><div class="by abs">Mira Holt</div><div class="meta abs">16k views</div><div class="ago abs">1 Month Ago</div><div class="price abs">$20</div></div>
    <div class="track abs" style="top:220px"><div class="thumb abs" role="img" aria-label="Album cover for Paper Boats"><b></b></div><div class="name abs">Paper Boats</div><div class="by abs">Mira Holt</div><div class="meta abs">12k views</div><div class="ago abs">1 Month Ago</div><div class="price abs">$20</div></div>
    <div class="track abs" style="top:340px;border-bottom:0"><div class="thumb abs" role="img" aria-label="Album cover for Salt And Cedar"><b></b></div><div class="name abs">Salt And Cedar</div><div class="by abs">Mira Holt</div><div class="meta abs">9k views</div><div class="ago abs">1 Month Ago</div><div class="price abs">$20</div></div>
  </aside>
</section>

<section class="event">
  <div class="event-band abs" role="img" aria-label="Glowing lava and fire backdrop"></div>
  <div class="event-photo abs" role="img" aria-label="Corwin Ashgrove in front of the fire backdrop"></div>
  <h2 class="event-kicker abs">Upcoming Event</h2>
  <div class="event-date abs"><i></i>Jun 15</div>
  <p class="event-text abs">Join the presentation of Ashgrove's latest release at Lanternhall Club in Los Angeles. Buy tickets now to listen to new &amp; famous hits by Ashgrove performed live.</p>
  <a class="btn btn-solid abs" href="#" style="left:672px;top:1872px;width:162px;height:40px;border-radius:4px">Buy Tickets</a>
</section>

<section class="news">
  <h2 class="section-title abs" style="left:64px;top:2098px;color:#fff">Latest News</h2>
  <p class="section-sub abs" style="left:64px;top:2146px">Here is the stories for all 3000 of our production, enjoy the movie and stay with us.</p>
  <article class="news-card abs" style="left:80px;background:linear-gradient(160deg,#c8c4e8,#5a4aa0 50%,#1a1530)" role="img" aria-label="CD cover with lightning and music notes"><p>Nam Lectus Nibh Consequat Auctor Turpis</p></article>
  <article class="news-card abs" style="left:431px;background:linear-gradient(160deg,#f0dcc8,#d89ab8 50%,#9ac0d8)" role="img" aria-label="CD cover with a painted heart collage"><p>Nam Lectus Nibh Consequat Auctor Turpis</p></article>
  <article class="news-card abs" style="left:782px;background:linear-gradient(160deg,#e8e8ea,#b0b8c8 50%,#d8d0c0)" role="img" aria-label="Corwin Ashgrove CD cover with title and photo"><p>Nam Lectus Nibh Consequat Auctor Turpis</p></article>
</section>

<footer>
  <div class="footer-line abs"></div>
  <div class="footer-photo abs" role="img" aria-label="Corwin Ashgrove in a hat outdoors"></div>
  <p class="footer-text abs">Mauris malesuada arcu eu posuere dapibus. Ut egestas tortor at leo egestas tincidunt. Nam tincidunt luctus tristique viverra. Mauris erat ante, egestas vitae dapibus vel.</p>
  <div class="footer-col abs" style="left:640px;top:2680px"><h4>Links</h4><a href="#">Home</a><a href="#">About Us</a><a href="#">Event</a><a href="#">Blog</a><a href="#">Contact</a></div>
  <div class="footer-col abs" style="left:824px;top:2680px"><h4>Newsletter</h4>
    <div class="email"><span>Enter Email</span><i><svg width="18" height="18" viewBox="0 0 20 20"><path d="M2 10l16-7-5 16-3-7z" fill="#000"/></svg></i></div>
    <div class="social" style="margin-top:20px"><i style="width:26px;height:26px"></i><i style="width:26px;height:26px"></i><i style="width:26px;height:26px"></i><i style="width:26px;height:26px"></i></div>
  </div>
  <p class="copyright abs">CopyRight© 2020 Company Name - All Rights Reserved.</p>
</footer>

</body>
</html>
```